Chinese Language Posters - TKUOME

We have created a series of African American heritage posters that will be distributed to Chinese Language Schools. We need a designer to create great posters for K-12 programs.

Quotes:
We have quotes from 6 important figures in Black History. We are seeking a designer to develop a poster utilizing at least one quote from each historical figure.

The designer MUST be fluent in Chinese in order to ensure the appropriate type and font.

Our organization, Tidewater Kestrel Union of Orchard Mentors Exchange, is a small organization of parents in the Bay Area working to encourage and support Black students learning the Chinese language.

Target Market(s)

These posters will be made available to Chinese Immersion schools (k-12).

Industry/Entity Type

Learning

Requirements
Must have
• Each poster should contain one quote from the list below.

Please create a poster of one historical figure and include their quote. The image can be abstract, landscape or an image of the figure.

The image should also include our logo. Our preferred logo is with the puffs but we understand if the clipart logo may be a better fit for the posters. (We LOVE the puffs logo though).
Nice to have
• I have uploaded images of each figure. The images can be used or a more abstract background. We are flexible. We would prefer a mix that includes figures and abstract backgrounds just focusing on the quote. We are open.

```html
<!DOCTYPE html>
<html lang="zh">
<head>
<meta charset="utf-8">
<title>Heritage Poster – TKUOME</title>
<link rel="stylesheet" href="https://fonts.googleapis.com/css2?family=Noto+Sans+SC:wght@400;500;700&family=Open+Sans:wght@400;600&display=swap">
<style>
  :root {
    --page: #ffffff;
    --poster-light: #f4f4f4;
    --poster-mid: #d9d9d9;
    --poster-dark: #b9b9b9;
    --ink: #2a2a2a;
    --quote-red: #d8261c;
    --quote-deep: #6e0d0a;
    --band: #1e1a19;
    --band-text: #ffffff;
    --badge: #ffffff;
    --badge-text: #c8201a;
  }
  html, body {
    margin: 0;
    padding: 0;
    width: 1200px;
    height: 1000px;
    overflow: hidden;
    background: var(--page);
  }
  .canvas {
    position: relative;
    width: 1200px;
    height: 1000px;
  }
  .poster {
    position: absolute;
    left: 277px;
    top: 48px;
    width: 633px;
    height: 897px;
    overflow: hidden;
    background:
      radial-gradient(ellipse 360px 420px at 300px 360px, var(--poster-light) 0%, rgba(244,244,244,0) 70%),
      linear-gradient(160deg, var(--poster-dark) 0%, var(--poster-mid) 35%, var(--poster-light) 60%, var(--poster-mid) 100%);
  }
  .portrait {
    position: absolute;
    left: 0;
    top: 38px;
    width: 530px;
    height: 650px;
  }
  .figure-name {
    position: absolute;
    right: 45px;
    top: 38px;
    text-align: right;
    color: var(--ink);
  }
  .figure-name .zh {
    font-family: "Noto Sans SC", sans-serif;
    font-size: 25px;
    font-weight: 400;
    letter-spacing: 1px;
    line-height: 1.2;
  }
  .figure-name .en {
    font-family: "Open Sans", sans-serif;
    font-size: 13px;
    font-weight: 600;
    margin-top: 2px;
  }
  .quote-zh {
    position: absolute;
    left: 0;
    right: 0;
    top: 642px;
    margin: 0;
    text-align: center;
    font-family: "Noto Sans SC", sans-serif;
    font-weight: 500;
    font-size: 61px;
    line-height: 72px;
    letter-spacing: 1px;
    background: linear-gradient(180deg, var(--quote-red) 0%, var(--quote-red) 45%, var(--quote-deep) 100%);
    -webkit-background-clip: text;
    background-clip: text;
    color: transparent;
    filter: drop-shadow(2px 3px 0 rgba(255,255,255,0.9));
  }
  .quote-band {
    position: absolute;
    left: 0;
    top: 817px;
    width: 633px;
    height: 47px;
    background: var(--band);
  }
  .quote-en {
    position: absolute;
    left: 45px;
    top: 13px;
    margin: 0;
    font-family: "Open Sans", sans-serif;
    font-size: 15px;
    color: var(--band-text);
    letter-spacing: 0.2px;
  }
  .org-badge {
    position: absolute;
    left: 516px;
    top: 805px;
    width: 70px;
    height: 70px;
    border-radius: 50%;
    background: var(--badge);
    display: flex;
    align-items: center;
    justify-content: center;
    font-family: "Open Sans", sans-serif;
    font-weight: 600;
    font-size: 12px;
    color: var(--badge-text);
  }
</style>
</head>
<body>
  <div class="canvas">
    <div class="poster">
      <svg class="portrait" role="img" aria-label="Watercolour portrait of the historical figure in a suit, painted in splashes of blue, red, orange, yellow and green" viewBox="0 0 530 650">
        <defs>
          <linearGradient id="portraitWash" x1="0" y1="0" x2="1" y2="1">
            <stop offset="0" stop-color="#7fa9d6"/>
            <stop offset="0.35" stop-color="#c94a4a"/>
            <stop offset="0.6" stop-color="#e48a3a"/>
            <stop offset="0.8" stop-color="#9fcf8a"/>
            <stop offset="1" stop-color="#6bb5d8"/>
          </linearGradient>
          <radialGradient id="portraitFade" cx="0.5" cy="0.45" r="0.6">
            <stop offset="0.5" stop-color="#fff" stop-opacity="1"/>
            <stop offset="1" stop-color="#fff" stop-opacity="0"/>
          </radialGradient>
          <mask id="portraitMask">
            <rect width="530" height="650" fill="url(#portraitFade)"/>
          </mask>
        </defs>
        <path mask="url(#portraitMask)" fill="url(#portraitWash)" opacity="0.8"
          d="M150 60 Q260 -10 370 60 Q400 150 380 260 Q360 330 300 370 L360 400 Q480 440 520 560 L510 620 L20 620 Q0 520 60 440 Q120 400 170 380 Q110 320 110 220 Q110 110 150 60 Z"/>
      </svg>

      <div class="figure-name">
        <div class="zh">伊莱亚斯 · 惠特福德 · 巴罗</div>
        <div class="en">Elias Whitford Barrow</div>
      </div>

      <p class="quote-zh">教育是打开金色自<br>由之门的钥匙。</p>

      <div class="quote-band">
        <p class="quote-en">Education is the key to unlock the golden door of freedom</p>
      </div>
      <div class="org-badge">TKUOME</div>
    </div>
  </div>
</body>
</html>
```